Trifold B2B flyer for software consulting/software futureproofness check / IT company

We need a flyer for a consulting offer for the company "VORANTEK GmbH".

The service involves the analysis and evaluation of software systems in companies; the target group consists of managing directors and IT managers of medium-sized companies in various industries.

The flyer should be modern, uncluttered, serious, and professional. It must inspire trust. A dark background would be preferable.

For content and layout, see PDF/PPTX "Software-Wandel-Fast-Scan-Konzept.pptx|.pdf".

In the appendix you will find further examples of VORANTEK designs, as well as the logo and other images.

-----------
We need a flyer for a consulting offering for the company “VORANTEK GmbH”.

The offering focuses on the analysis and evaluation of software systems within companies. The target audience is managing directors/CEOs and IT managers of mid-sized companies across various industries.

The flyer should be modern, clean, serious, and professional. It must build trust. A dark background is preferred.

Please refer to the PDF/PPTX “Software-Wandels-Fast-Scan-konzept.pptx|.pdf” for the content and the layout/ordering of the sections.

Attached you will also find additional examples of VORANTEK designs, as well as the logo and further images.

Target Market(s)

Medium businesses, various industries. Target group: CEO, CIO, IT lead

Industry/Entity Type

Medium-Businesses, various Industries.

Font styles to use
Sans Serif
Other font styles liked:
• Myriad

Colors

Designer to choose colors to be used in the design.

Requirements
Must have
• Branding of my company, professional, stylish, clean, trustful design

```html
<!DOCTYPE html>
<html lang="de">
<head>
<meta charset="utf-8">
<title>Software-Wandels-Fast-Scan – VORANTEK GmbH</title>
<link href="https://fonts.googleapis.com/css2?family=Poppins:wght@400;600;700&display=swap" rel="stylesheet">
<style>
  :root {
    --bg: #01060f;
    --bg-mid: #030a17;
    --blue: #2e6fc4;
    --blue-deep: #123a7a;
    --text: #e9edf3;
    --text-soft: #d6dce5;
    --white: #ffffff;
    --rule: rgba(120,140,170,.25);
  }
  * { margin: 0; padding: 0; box-sizing: border-box; }
  html, body { width: 1200px; height: 848px; overflow: hidden; background: var(--bg); }
  body { font-family: "Poppins", sans-serif; color: var(--text); }
  .flyer { position: relative; width: 1200px; height: 848px; background: var(--bg); overflow: hidden; }
  .panel-band { position: absolute; top: 0; left: 403px; width: 404px; height: 848px; background: var(--bg-mid); }
  .pattern { position: absolute; }
  .pattern--top { right: 0; top: 0; width: 240px; height: 255px;
    background: radial-gradient(ellipse at 75% 35%, rgba(30,80,170,.55), rgba(10,30,70,.35) 45%, transparent 72%); }
  .pattern--bottom { left: 0; bottom: 0; width: 240px; height: 290px;
    background: radial-gradient(ellipse at 30% 70%, rgba(30,80,170,.45), rgba(10,30,70,.3) 45%, transparent 72%); }
  .arrow { position: absolute; top: 150px; width: 94px; height: 118px; }
  .arrow--one { left: 369px; }
  .arrow--two { left: 769px; }
  .swoosh { position: absolute; left: 450px; top: 512px; width: 295px; height: 200px; }

  .title { position: absolute; left: 46px; top: 64px; font-size: 24px; font-weight: 700; line-height: 28px; color: var(--white); letter-spacing: .2px; }
  .subtitle { position: absolute; left: 46px; top: 125px; font-size: 14.5px; line-height: 19.5px; color: var(--text-soft); }
  .intro { position: absolute; left: 455px; top: 76px; width: 300px; text-align: center; font-size: 13px; line-height: 18.3px; color: var(--text-soft); }

  .heading { position: absolute; top: 262px; font-size: 22.5px; font-weight: 700; color: var(--white); letter-spacing: .2px; }
  .heading--q { left: 37px; }
  .heading--v { left: 460px; }
  .heading--e { left: 847px; }

  .list { position: absolute; list-style: none; }
  .list li { position: relative; }
  .list li::before { content: ""; position: absolute; width: 8px; height: 10px; background: var(--blue); clip-path: polygon(0 0, 100% 50%, 0 100%); }
  .list b { font-weight: 700; }

  .list--questions { left: 56px; top: 312px; width: 300px; font-size: 14px; line-height: 19.7px; }
  .list--questions::before { content: ""; position: absolute; left: -15px; top: 10px; width: 1px; height: 190px; background: var(--rule); }
  .list--questions li { margin-bottom: 14px; }
  .list--questions li::before { left: -18px; top: 6px; }

  .list--steps { left: 477px; top: 309px; width: 272px; font-size: 13px; line-height: 18.3px; }
  .list--steps::before { content: ""; position: absolute; left: -15px; top: 10px; width: 1px; height: 160px; background: var(--rule); }
  .list--steps li { margin-bottom: 10px; }
  .list--steps li::before { left: -18px; top: 6px; }

  .list--results { left: 866px; top: 309px; width: 300px; font-size: 13.2px; line-height: 18.3px; }
  .list--results li { margin-bottom: 10px; }
  .list--results li::before { left: -17px; top: 4px; }

  .sub-heading { position: absolute; font-size: 14.5px; font-weight: 700; color: var(--white); }
  .small-list { position: absolute; list-style: none; font-size: 13.2px; line-height: 18.3px; }
  .small-list li { position: relative; }
  .small-list li::before { content: ""; position: absolute; left: -16px; top: 4px; width: 8px; height: 10px; background: var(--blue); clip-path: polygon(0 0, 100% 50%, 0 100%); }
  .note { position: absolute; left: 848px; font-size: 13.2px; line-height: 18.3px; }
  .note b { font-weight: 700; }
</style>
</head>
<body>
<main class="flyer">
  <div class="panel-band"></div>
  <div class="pattern pattern--top" role="img" aria-label="Dekoratives Dreiecksmuster in Blautönen"></div>
  <div class="pattern pattern--bottom" role="img" aria-label="Dekoratives Dreiecksmuster in Blautönen"></div>

  <svg class="arrow arrow--one" viewBox="0 0 94 118"><path d="M0 10 Q0 -3 12 4 L88 48 Q98 59 88 70 L12 114 Q0 121 0 108 Z" fill="#2e6fc4"/></svg>
  <svg class="arrow arrow--two" viewBox="0 0 94 118"><path d="M0 10 Q0 -3 12 4 L88 48 Q98 59 88 70 L12 114 Q0 121 0 108 Z" fill="#2e6fc4"/></svg>

  <svg class="swoosh" viewBox="0 0 295 200">
    <defs>
      <linearGradient id="swooshFill" x1="0" y1="0.4" x2="1" y2="0">
        <stop offset="0" stop-color="#0a1a35" stop-opacity="0"/>
        <stop offset="0.55" stop-color="#123a7a" stop-opacity="0.55"/>
        <stop offset="1" stop-color="#2a64b8"/>
      </linearGradient>
    </defs>
    <path d="M5 40 Q8 33 30 30 L270 2 Q292 0 289 22 L232 200 L5 200 Z" fill="url(#swooshFill)"/>
  </svg>

  <h1 class="title">SOFTWARE-WANDELS-<br>FAST-SCAN</h1>
  <p class="subtitle">Bestandssysteme: weiter investieren,<br>modernisieren oder ersetzen?</p>

  <p class="intro">Der Fast-Scan dient der schnellen<br>Orientierung und Objektivierung.<br>Er stellt die Basis für eine detaillierte<br>Analyse des Bestandssystems in Punkto<br>Zukunftsfähigkeit und<br>Handlungsoptionen dar.</p>

  <h2 class="heading heading--q">FRAGESTELLUNGEN</h2>
  <ul class="list list--questions">
    <li>Was sind die <b>realen Risiken</b> (Betrieb, Stabilität, Abhängigkeiten, Know-how)?</li>
    <li>Wo liegen die größten Kostentreiber<br>(Betriebskosten, Change-Kosten,<br>Folgekosten)?</li>
    <li>Welche drei Wege sind grundsätzlich realistisch: <b>Invest / Modernize / Replace?</b></li>
    <li>Was müssen wir <b>jetzt</b> wissen, um innerhalb von 5–10 Tagen sauber entscheiden zu können?</li>
  </ul>

  <h2 class="heading heading--v">VORGEHEN</h2>
  <ul class="list list--steps">
    <li><b>Kickoff (60–90 Min):</b> Ziel, Kontext,<br>Entscheidungsdruck, verfügbare Artefakte</li>
    <li><b>Sichtung &amp; Analyse:</b> max. 10 Artefakte<br>(Kosten, Incidents, Roadmap, Architektur-<br>Skizze, Vendor-Info)</li>
    <li><b>2 Interviews (je 60–90 Min):</b> CIO/Owner +<br>Head of Engineering/Tech Lead</li>
    <li><b>Ergebnisgespräch (60 Min):</b> Ergebnisse,<br>Lücken, Empfehlung, nächster Schritt</li>
  </ul>

  <h3 class="sub-heading" style="left:460px; top:562px">SCOPE:</h3>
  <ul class="small-list" style="left:476px; top:588px; width:200px">
    <li>1 System</li>
    <li>1–2 Calls + Doku-Sichtung</li>
    <li>Ergebnis als kompakte Entscheidungsunterlagen</li>
  </ul>

  <h3 class="sub-heading" style="left:460px; top:684px">NICHT ENTHALTEN:</h3>
  <ul class="small-list" style="left:476px; top:708px; width:250px">
    <li>Detail-Spezifikation, Ausschreibung, Umsetzung, Tool-Auswahlprozess im Vollumfang</li>
  </ul>

  <h2 class="heading heading--e">ERGEBNISSE / LIEFEROBJEKTE</h2>
  <ul class="list list--results">
    <li><b>Decision Snapshot:</b> Status, Top-Risiken,<br>wesentliche TCO-Treiber, offene<br>Entscheidungsfragen (One-Pager)</li>
    <li style="margin-bottom:13px"><b>3-Optionen-Skizze:</b> Modernize / Replace /<br>Invest mit Pros/Cons und Abhängigkeiten<br>(One-Pager)</li>
    <li style="margin-bottom:6px"><b>&nbsp;Gap-Liste:</b> Welche Informationen fehlen für<br>eine saubere Entscheidung (Max. 10 Punkte)</li>
    <li><b>Go/No-Go-Empfehlung:</b><br>Mögliche nächste Schritte und<br>Handlungs-optionen</li>
  </ul>

  <h3 class="sub-heading" style="left:848px; top:594px">PREIS &amp; DAUER:</h3>
  <ul class="small-list" style="left:865px; top:619px; width:300px">
    <li>Preis: 3.500–5.000 € (zzgl. USt)</li>
    <li>Dauer: 1 Woche</li>
  </ul>
  <p class="note" style="top:660px">(Festpreis, abhängig von der Komplexität)</p>
  <p class="note" style="top:684px">Upgrade möglich zum umfassenden<br><b>Software Wandels-Check</b></p>
</main>
</body>
</html>
```